Urgent - brand new business card for a startup technical advisory and incubation business in Sydney

We need a brand new business card design for BrightForge. We are a startup technical advisory and incubation business based in Sydney Australia. We work with entrepreneurs and innovators to help rapidly and efficiently turn their ideas into reality and to ensure they have the technical platform required for growth.

Our name is partly inspired by our love of lean product development methods and the lean startup movement.

We would like clean, uncluttered designs that feature our two logo colours and communicate a professional but creative, in-touch and entrepreneurial business.

PLEASE SEE MUST HAVE PRIORITIES FOR DRAFT CONTACT INFORMATION AND OTHER DESIRED TEXT ON CARD.
Updates

We have now updated the brief to include draft business card contact information and also some additional desired text to feature on the card design.    Please review the Must Have priorities.

Also final updated source files for the horizontal and vertical versions have now been uploaded and should be used for any designs.

Thanks!

Target Market(s)

Entrepeneurs, innovators, startup investors looking for a strong product development partner

Industry/Entity Type

Business

Requirements
Must have
• Feature our two logo colours
Be a relatively clean, pared back overall design - quite minimalist

Updated source files (AI) for vertical and horizontal layouts attached.

Draft contact information for business card:
Neil Barton
Founder & CTO
Phone: +61 427 555123
Email: xxxx@brightforge.com
Skype: xxxxxbarton
Twitter: nbarton

www.brightforge.com

We would also like the overall design to include the phrase "You have great ideas. Let us make them happen." (probably in a reasonably subtle way)

Nice to have
• Inspire me! Double-sided designs are fine with logo, phrase, (URL?) on one side and contact details on other (+ any other design elements)

Logo on business card can be either with lightbulb above the wording as per example here or to the left of the BrightForge wording - both layouts in files provided.
Should not have
• Shouldn't look like a Pentara Suite business card template :-)

```html
<!DOCTYPE html>
<html lang="en">
<head>
<meta charset="utf-8">
<title>BrightForge — Business Card</title>
<link href="https://fonts.googleapis.com/css2?family=Archivo+Narrow:wght@700&family=Libre+Franklin:ital,wght@0,400;1,400&display=swap" rel="stylesheet">
<style>
  :root {
    --brand-blue: #00aeef;
    --brand-ink: #1c2331;
    --text: #222628;
    --paper: #ffffff;
    --backdrop: #ffffff;
    --shadow: rgba(0, 0, 0, 0.16);
  }
  * { margin: 0; padding: 0; box-sizing: border-box; }
  html, body {
    width: 1200px;
    height: 900px;
    overflow: hidden;
    background: var(--backdrop);
  }
  .stage {
    position: relative;
    width: 1200px;
    height: 900px;
  }
  .card {
    position: absolute;
    top: 198px;
    width: 288px;
    height: 504px;
    background: var(--paper);
    box-shadow: 0 2px 8px var(--shadow);
  }
  .card--front { left: 262px; }
  .card--back { left: 650px; }

  .brand-mark {
    position: absolute;
    left: 0;
    right: 0;
    top: 150px;
    display: flex;
    flex-direction: column;
    align-items: center;
  }
  .brand-mark__dot {
    width: 88px;
    height: 88px;
    border-radius: 50%;
    background: var(--brand-blue);
    margin-bottom: 26px;
  }
  .brand-mark__name {
    font-family: "Archivo Narrow", "Arial Narrow", sans-serif;
    font-weight: 700;
    font-size: 44px;
    line-height: 1;
    letter-spacing: -0.5px;
    color: var(--brand-ink);
  }

  .person {
    position: absolute;
    left: 42px;
    top: 126px;
  }
  .person__name {
    font-family: "Archivo Narrow", "Arial Narrow", sans-serif;
    font-weight: 700;
    font-size: 23px;
    line-height: 26px;
    color: var(--brand-blue);
  }
  .person__role {
    font-family: "Libre Franklin", Arial, sans-serif;
    font-size: 14px;
    line-height: 18px;
    color: var(--text);
  }

  .contact {
    position: absolute;
    left: 42px;
    top: 319px;
    font-family: "Libre Franklin", Arial, sans-serif;
    font-size: 12.5px;
    line-height: 17px;
    color: var(--text);
  }
  .contact__row { display: flex; }
  .contact__label { width: 50px; color: #444a4d; }
  .contact__value { color: var(--brand-ink); }

  .website {
    position: absolute;
    left: 42px;
    top: 402px;
    font-family: "Libre Franklin", Arial, sans-serif;
    font-size: 12.5px;
    line-height: 17px;
    color: var(--brand-ink);
  }
  .tagline {
    position: absolute;
    left: 42px;
    top: 434px;
    font-family: "Libre Franklin", Arial, sans-serif;
    font-style: italic;
    font-size: 12.5px;
    line-height: 17px;
    color: var(--brand-blue);
  }
</style>
</head>
<body>
  <main class="stage">
    <section class="card card--front" aria-label="Card front">
      <div class="brand-mark">
        <span class="brand-mark__dot" aria-hidden="true"></span>
        <span class="brand-mark__name">BrightForge</span>
      </div>
    </section>

    <section class="card card--back" aria-label="Card back">
      <div class="person">
        <h1 class="person__name">Neil Barton</h1>
        <p class="person__role">Founder &amp; CTO</p>
      </div>

      <dl class="contact">
        <div class="contact__row"><dt class="contact__label">Phone</dt><dd class="contact__value">+61 427 555123</dd></div>
        <div class="contact__row"><dt class="contact__label">Email</dt><dd class="contact__value">xxxx@brightforge.com</dd></div>
        <div class="contact__row"><dt class="contact__label">Skype</dt><dd class="contact__value">xxxxxbarton</dd></div>
        <div class="contact__row"><dt class="contact__label">Twitter</dt><dd class="contact__value">@nbarton</dd></div>
      </dl>

      <p class="website">www.brightforge.com</p>

      <p class="tagline">You have great ideas.<br>Let us make them happen.</p>
    </section>
  </main>
</body>
</html>
```